Plakat-Design für eine Werbeschild für ein Geflügelhof
Zielgruppe
Wir sind ein Geflügelhof, Landhandel, Hofladen, Eier stehen seit über 100 Jahren für Hof Lernstedt, artgerechte Tierhaltung und Artikelvielfalt machen uns bekannt.
Aufgabenstellung
Das Werbeschild wird auf dem Hof aufgestellt und soll den Weg zum Hof zeigen.
- die Maße vom Schild: 1,50m breit x 2,40m hoch
- Grafiken werden als .ai und .pdf benötigt
- Logo ist hochgelagen
- Foto von unserer Vorstellung ist hochgeladen
Das Schild muss 400 m RECHTS drauf gedruckt haben.
Falls es zu breit wäre, könnte das Logo ja vielleicht auch über Hof Lernstedt.
Das ganze wird bei plakwerk auf eine MetaPlanko-Platte in den Druck gegeben.

```html
<!DOCTYPE html>
<html lang="de">
<head>
<meta charset="utf-8">
<title>Hof Lernstedt – Wegweiser</title>
<link rel="stylesheet" href="https://fonts.googleapis.com/css2?family=Open+Sans:wght@500;600;700&display=swap">
<style>
  :root {
    --farm-green: #216b34;
    --sky-blue: #009fe0;
    --paper-white: #ffffff;
    --hen-brown: #c9b79f;
    --hen-cream: #f3ead2;
  }
  html, body {
    margin: 0;
    padding: 0;
    overflow: hidden;
    background: var(--paper-white);
  }
  .sign {
    position: relative;
    width: 750px;
    height: 1200px;
    overflow: hidden;
    font-family: "Open Sans", Arial, sans-serif;
    background: linear-gradient(
      to bottom,
      var(--paper-white) 0px,
      var(--paper-white) 351px,
      var(--sky-blue) 461px,
      var(--sky-blue) 798px,
      var(--farm-green) 798px,
      var(--farm-green) 1200px
    );
  }
  .brand-mark {
    position: absolute;
    left: 273px;
    top: 39px;
    width: 184px;
    height: 184px;
    border-radius: 50%;
    background: var(--farm-green);
  }
  .brand-name {
    position: absolute;
    left: 0;
    top: 252px;
    width: 750px;
    margin: 0;
    text-align: center;
    font-size: 62px;
    font-weight: 700;
    line-height: 1;
    color: var(--farm-green);
  }
  .shop-badge {
    position: absolute;
    left: 141px;
    top: 372px;
    width: 476px;
    height: 476px;
    border-radius: 50%;
    background: var(--farm-green);
  }
  .shop-badge-inner {
    position: absolute;
    left: 17px;
    top: 17px;
    width: 432px;
    height: 432px;
    border-radius: 50%;
    border: 5px solid var(--paper-white);
    display: flex;
    align-items: center;
    justify-content: center;
  }
  .shop-badge-text {
    margin: 0 0 40px;
    text-align: center;
    color: var(--paper-white);
    font-size: 34px;
    font-weight: 500;
    line-height: 1.45;
  }
  .hen {
    position: absolute;
    border-radius: 45% 45% 40% 40%;
  }
  .hen-left {
    left: 93px;
    top: 693px;
    width: 164px;
    height: 228px;
    background: linear-gradient(160deg, #d6c6b0, var(--hen-brown) 60%, #a9957c);
  }
  .hen-right {
    left: 555px;
    top: 712px;
    width: 159px;
    height: 215px;
    background: linear-gradient(160deg, #fbf5e6, var(--hen-cream) 60%, #e6d7a8);
  }
  .direction-arrow {
    position: absolute;
    left: 340px;
    top: 855px;
  }
  .distance {
    position: absolute;
    left: 0;
    top: 1040px;
    width: 750px;
    margin: 0;
    text-align: center;
    color: var(--paper-white);
    font-size: 68px;
    font-weight: 600;
    line-height: 1;
  }
</style>
</head>
<body>
  <main class="sign">
    <div class="brand-mark" aria-hidden="true"></div>
    <h1 class="brand-name">Hof Lernstedt</h1>

    <div class="shop-badge">
      <div class="shop-badge-inner">
        <p class="shop-badge-text">Einkauf auf dem<br>Bauernhof</p>
      </div>
    </div>

    <div class="hen hen-left" role="img" aria-label="Illustration eines braun-beigen Huhns"></div>
    <div class="hen hen-right" role="img" aria-label="Illustration eines hellen, cremefarbenen Huhns"></div>

    <svg class="direction-arrow" width="180" height="160" viewBox="0 0 180 160" aria-label="Pfeil nach rechts abbiegen" role="img">
      <path d="M5 155 V38 H140" fill="none" stroke="#ffffff" stroke-width="21"/>
      <polygon points="138,7 171,38 138,70" fill="#ffffff"/>
    </svg>

    <p class="distance">400 m rechts</p>
  </main>
</body>
</html>
```